Web Design with a Twist! Not cheap design

Please note that this project is ending at 5pm on Tuesday the 28th of September, Australian Western Standard Time!!

Please also note that this project has now been guaranteed!

This project involves three primary elements:
* Logo design;
* Web design - of additional pages and page elements to fit into a site that is already in design/development;
* Graphic design - various images used on the site.

The following materials are included for the project:
* Project requirements
* Company / Site name
* Company / Site description
* Wireframes for new pages / page elements
* Screenshots of existing designs and accompanying definition of constraints for new designs
* PSDs for existing site designs
* Technical requirements for designs
* Content (to guide designs)

Project Requirements:

* Logo design:
This is a new company / site, so we need a new logo. We want to see what you come up with here without giving too much direction that may restrict creativity. If desired, you may find possible guidance through considering the company name, company description, and the existing site designs. Please note that the current logo in the site is for placeholder purposes only.

* Web design:
We need the following pages (and features) to be designed for the site:
• Home page
• Advertise page
• How it works page
We’ve provided some wireframes for the pages, however we definitely don't want you to be guided by the layout/styling at all - the wireframes are only there to indicate the features that we require on each page only. So please ignore all aspects of the wireframes except for the indications of features and functionality.

* Graphic design:
We need various images to be designed throughout the site. These include:
• The image at the top of the ‘Home’ page – please note we will provide some direction on this asap
• The image at the top of the ‘Advertise’ page – please note we will provide some direction n this asap
• The image at the top of the ‘How it Works’ pages
• The images that accompany each of the left hand menu items on the ‘How it Works’ pages (the main images & thumbnails if that’s part of your design). Please note that these images need to be constructed to match the Headlines for each of the ‘What’, ‘Who’, ‘Where’, etc menu items. These Headlines (and some descriptive text) can be found in the Content section at the end of this brief.
• The map of Australia for the ‘Home’ page
• The images to accompany the pricing section of the ‘Advertise’ page
• The variations of the ‘Life in the search lane’ images that are used on the ‘Home’, ‘Advertise’, and ‘How it Works’ pages. Please note that if you want to use different imagery (or no imagery, dependent upon your design) for the Home and Advertise pages then this is your call.

Company Name:
TaskBloom

Company / Site description:
This site will provide a means for contractors ('advertisers') to easily specify and advertise their services, coupled with a means for employers (‘buyers’) to easily seek out and contact these people.
The site will cater for contractor-side advertisements only; job postings will not be accommodated (turning the traditional job advertisement model on its head).
In general, the functionality of the site is somewhat like a mashup of sites like crewvault.com and stayvane.com. The site will incorporate the following primary features of contractor profile display and search, company profile display, (and an availability calendar for v2 release).

Constraints for designs:
On some of the existing designs you will notice that a number of the elements of the site have already been designed. When constructing your designs, please work in accordance with the following constraints:

You have to keep:
• Colour scheme in the header
• Colour scheme in the top navigation buttons (including text colour and background colour)
• Colour scheme for the buttons like on the Register page

You can ignore:
• The existing placeholder logo
• Border, layout, and colour scheme for page elements (like the lines around and inside the register section on the Register page)
• Design of text fields
• Font colour scheme throughout the site – the orange and grey headlines and body text
• Design and colour scheme of the map of Australia
• The breadcrumbs (whether or not they appear, and their layout, styling, colour scheme etc)
• Dropdown styling (assuming you had to make some; currently not on any pages we’re asking you to do) like on the Browse Profession page
• Profile styling (for the home page featured profiles) like on the Browse Profession page
• Footer styling
• Anything else we haven’t explicitly asked you to keep

Technical requirements for design:
Any site designs in either Layered Photoshop files (PSD's) or Illustrator Drawings (AI). RGB Color. Must fit current site design, we work to 1024 wide screens. Usuable area is defined in site designs that are attached in the Photoshop documents; it's around 960px.
Logo work needs to be Illustrator Drawings (AI) and EPS. Need CMYK images for printing and RGB for screen. Logos must include any special fonts that are used as TTF or Open Type. Logos need Color, Monochrome, Reversed and both Tall and Wide usages.

Content for the 'How it Works' pages - this content should guide the images that appear on each page.
* What
Headline: TaskBloom brings contractors and employers together
Descriptive text: (turns the traditional job search model on its head)
* Who
Headline: TaskBloom is for highly skilled professionals and fast moving companies
Descriptive text:
* Where
Headline: Anywhere in Australia, TaskBloom is working by your side
Descriptive text:
* Why
Headline: There are more than 1 million reasons to love TaskBloom
Descriptive text: In Australia, there are 1 million people who work as contractors in their main job, and a further 100,000 people who are contractors in their second job. That’s a lot of contractors!
* When
Headline: TaskBloom is forming partnerships 24 hours a day
Descriptive text:
* How
Headline: Life in the search lane, with TaskBloom
Descriptive text: Advertise on TaskBloom now, and get your life in the search lane.

Remember
Just remember the wireframes we have submitted are just a guide – we want to see your creativity shine. And above all else - have fun!
Thank you.
Updates

Please note the deadline for this design competition 5pm on Tuesday the 28th of September, Australian Western Standard Time.

Just under 3 days away!

The deadline of the project will soon be updated to reflect this.

Hi Designers!

Just to be 100% clear about the deadline - the timer is currently showing 7 hours too many. In other words, the project will end 7 hours before the timer finishes.

I will send a notification if the timer starts to display the correct time. So until then, please remember that the deadline is earlier than it seems!

Thanks

Hi Designers,

A couple of really important points:

Firstly - if everyone could please stick to the theme that we provided in the Photoshop files that would be excellent. It is not possible for us to create a new theme. We're dealing with very tight deadlines, so please just provide designs that fit within the current theme.

Secondly, we were really hoping for more illustrations / graphics to be provided in the designs. We're not a fan of the stock photos of generic business people. So please send through designs that incorporate illustrations / graphics for any imagery.

Also just a reminder that this competition is still ending 7 hours earlier than the timer currently displays.

Thanks.

Target Market(s)

The ‘advertiser’ target market for the site is white collar professionals, in all types of industries. The site will be catering for premium contractors only. The site will be catering for both 'in person' contractors, as well as 'knowledge economy' contractors. The site will not be seeking to compete with gigmora.com, plixo.com, taskrune.com, or similar sites.

The advertiser target market will also encompass companies and labour hire agencies that have contractors in their workforce.

The ‘buyer’ target market will encompass employers, recruitment agents, and member-to-member hiring.

Industry/Entity Type

Contractor

Requirements
Must have
• As per overview
Nice to have
• As per overview
Should not have
• As per overview

```html
<!DOCTYPE html>
<html lang="en">
<head>
<meta charset="utf-8">
<title>TaskBloom – Find the right person for any job</title>
<link rel="stylesheet" href="https://fonts.googleapis.com/css2?family=Arimo:wght@400;700&display=swap">
<style>
:root{
  --orange:#f26a0f;
  --orange-soft:#f6a57a;
  --header-top:#7a879c;
  --header-bottom:#8c98ad;
  --tab:#c7ccd5;
  --tab-text:#7f8898;
  --tab-active:#eef1f5;
  --panel:#eef3f8;
  --panel-border:#c8d6e4;
  --bubble:#e2eaf3;
  --text:#3c4452;
  --muted:#a0a8b5;
  --heading-grey:#6a7a90;
  --green:#7ec66a;
  --white:#ffffff;
}
*{box-sizing:border-box;margin:0;padding:0}
html,body{width:1200px;height:900px;overflow:hidden;background:var(--white)}
body{position:relative;font-family:"Arimo",Arial,sans-serif;color:var(--text)}
.site-header{position:absolute;left:0;top:0;width:1200px;height:144px;background:linear-gradient(180deg,var(--header-top),var(--header-bottom))}
.brand{position:absolute;left:36px;top:0;width:168px;height:180px;background:var(--orange);display:flex;align-items:flex-end;justify-content:center;padding-bottom:22px;z-index:3}
.brand-name{color:var(--white);font-weight:700;font-size:27px;letter-spacing:-.5px}
.main-nav{position:absolute;top:104px;left:234px;display:flex;gap:14px}
.nav-tab{height:40px;border-radius:10px 10px 0 0;background:var(--tab);color:var(--tab-text);font-weight:700;font-size:21px;display:flex;align-items:center;justify-content:center}
.nav-tab.home{width:46px;background:var(--tab-active)}
.nav-tab.browse{width:124px}
.nav-tab.advertise{width:148px}
.nav-tab.login{width:110px}
.top-search{position:absolute;left:864px;top:104px;display:flex}
.top-search .field{width:248px;height:30px;background:var(--white);border-radius:3px 0 0 3px;display:flex;align-items:center;padding-left:10px;gap:8px;font-size:17px;color:#666}
.top-search .go{width:48px;height:30px;background:#5e6b80;color:var(--white);font-weight:700;font-size:17px;display:flex;align-items:center;justify-content:center;border-radius:0 3px 3px 0}
.breadcrumb{position:absolute;left:234px;top:164px;font-size:20px;color:var(--muted)}
.hero{position:absolute;left:36px;top:200px;width:1128px;height:280px}
.hero-art{position:absolute;inset:0;background:linear-gradient(180deg,#9aa3ab 0%,#c6cbcf 38%,#8c8a58 58%,#7c6a3a 78%,#5a4b30 100%)}
.hero-title{position:absolute;left:28px;top:26px}
.hero-title span{display:inline-block;background:var(--orange);color:var(--white);font-weight:700;font-size:45px;line-height:1;padding:10px 12px 12px 10px}
.hero-title span + br + span{margin-top:0}
.hero-lead{position:absolute;left:30px;top:192px;width:520px;color:var(--white);font-size:21px;line-height:25px;letter-spacing:-.3px}
.btn{background:var(--orange);color:var(--white);font-weight:700;display:flex;align-items:center;justify-content:center;border-radius:3px}
.hero .btn{position:absolute;left:990px;top:218px;width:134px;height:42px;font-size:19px}
.search-panel{position:absolute;left:36px;top:512px;width:436px;height:224px;background:var(--panel);border:1px solid var(--panel-border);padding:22px 26px}
.search-panel h2{color:var(--orange);font-size:26px;font-weight:400;margin-bottom:14px}
.search-panel .field{width:378px;height:34px;border:2px solid #a9b3bf;background:var(--white);display:flex;align-items:center;gap:8px;padding-left:8px;font-size:20px;color:#555}
.state-row{display:flex;align-items:center;gap:18px;margin-top:14px;font-size:15px;color:#6a7280}
.select{width:168px;height:28px;border:1px solid #a9b3bf;background:var(--white);display:flex;align-items:center;justify-content:space-between;padding-left:6px;font-size:15px}
.select i{width:24px;height:100%;background:#b7c0cb;display:flex;align-items:center;justify-content:center}
.search-panel .btn{position:absolute;right:26px;bottom:20px;width:116px;height:38px;font-size:19px}
.panel-notch{position:absolute;left:472px;top:520px}
.intro{position:absolute;left:502px;top:528px;width:300px;font-size:20px;line-height:25px;color:var(--muted)}
.featured{position:absolute;left:826px;top:504px;width:338px}
.featured h3{font-size:20px;font-weight:400;color:var(--heading-grey);margin-bottom:14px}
.quote{position:relative;height:132px;background:var(--bubble);margin-left:4px;margin-bottom:14px;padding:14px 120px 0 16px;font-size:16px;line-height:21px;color:#556173}
.quote .who{position:absolute;left:70px;bottom:8px;font-size:11px;color:var(--orange)}
.quote .portrait{position:absolute;right:14px;top:18px;width:84px;height:84px;background:linear-gradient(160deg,#c8b9a4,#6d5b4c)}
.quote.alt{padding:14px 16px 0 120px}
.quote.alt .portrait{left:14px;right:auto;top:14px;width:80px;height:80px;background:linear-gradient(160deg,#d4c5b0,#7e6c59)}
.quote.alt .who{left:50px}
.quote .tail{position:absolute;bottom:-14px}
.signup{position:absolute;left:830px;top:850px;width:334px;height:50px;background:var(--green);color:var(--white);font-weight:700;font-size:21px;display:flex;align-items:center;justify-content:center;border-radius:3px 3px 0 0}
.teasers{position:absolute;left:36px;top:758px;display:flex;gap:40px}
.teaser{width:226px}
.teaser h4{font-size:20px;font-weight:400;color:var(--heading-grey);margin-bottom:10px}
.teaser .slot{height:60px;border:2px solid #f8c9ad;display:flex;align-items:center;justify-content:center;font-size:15px;color:var(--orange-soft)}
.teaser p{margin-top:14px;font-size:16px;color:#98a0ac}
.fade{position:absolute;left:0;top:760px;width:1200px;height:140px;background:linear-gradient(180deg,rgba(255,255,255,0),rgba(255,255,255,.9));pointer-events:none}
</style>
</head>
<body>
<header class="site-header">
  <div class="brand"><span class="brand-name">TaskBloom</span></div>
  <nav class="main-nav">
    <div class="nav-tab home"><svg width="20" height="18" viewBox="0 0 20 18"><path d="M10 1 1 9h3v8h4v-5h4v5h4V9h3z" fill="#7f8898"/></svg></div>
    <div class="nav-tab browse">BROWSE</div>
    <div class="nav-tab advertise">ADVERTISE</div>
    <div class="nav-tab login">LOG IN</div>
  </nav>
  <div class="top-search">
    <div class="field"><svg width="14" height="14" viewBox="0 0 14 14"><circle cx="6" cy="6" r="4.5" fill="none" stroke="#777" stroke-width="1.6"/><path d="M9.5 9.5 13 13" stroke="#777" stroke-width="1.8"/></svg>Find a contractor</div>
    <div class="go">Go</div>
  </div>
</header>

<div class="breadcrumb">Home</div>

<section class="hero">
  <div class="hero-art" role="img" aria-label="Open grassy field under a cloudy sky with a lone tree"></div>
  <h1 class="hero-title"><span>Find the right person</span><br><span>for any job</span></h1>
  <p class="hero-lead">TaskBloom helps connect the right people with the right jobs, no matter how big or small</p>
  <a class="btn">Learn more...</a>
</section>

<section class="search-panel">
  <h2>Find highly skilled professionals</h2>
  <div class="field"><svg width="16" height="16" viewBox="0 0 14 14"><circle cx="6" cy="6" r="4.5" fill="none" stroke="#777" stroke-width="1.6"/><path d="M9.5 9.5 13 13" stroke="#777" stroke-width="1.8"/></svg>Find a contractor</div>
  <div class="state-row">Search in any or all states:
    <div class="select">Any state<i><svg width="10" height="7" viewBox="0 0 10 7"><path d="M0 0h10L5 7z" fill="#556"/></svg></i></div>
  </div>
  <a class="btn">Search</a>
</section>
<svg class="panel-notch" width="18" height="30" viewBox="0 0 18 30"><path d="M0 0 18 15 0 30z" fill="#eef3f8"/></svg>

<p class="intro">Lorem ipsum dolor sit amet, consectetur adipiscing elit. Pellentesque velit mauris, eleifend et malesuada et, viverra sed velit. Suspendisse feugiat odio eu velit varius iaculis. Cras vitae lacus est.</p>

<aside class="featured">
  <h3>Featured Businesses</h3>
  <div class="quote">I've picked up more jobs since starting with TaskBloom. They've been great and support is top notch!
    <span class="portrait" role="img" aria-label="Portrait of a featured business owner"></span>
    <span class="who">Ellis Marwood, Quillfern Studio</span>
    <svg class="tail" style="right:20px" width="20" height="14" viewBox="0 0 20 14"><path d="M0 0h20L18 14z" fill="#e2eaf3"/></svg>
  </div>
  <div class="quote alt">So easy to use. I was set up in no time. I can't recommend this service enough.
    <span class="portrait" role="img" aria-label="Portrait of a featured business owner"></span>
    <span class="who">Dorian Pell, Brightlane Works</span>
    <svg class="tail" style="left:20px" width="20" height="14" viewBox="0 0 20 14"><path d="M0 0h20L2 14z" fill="#e2eaf3"/></svg>
  </div>
</aside>

<section class="teasers">
  <div class="teaser"><h4>Lorem Ipsum dolor</h4><div class="slot">Some imagery that relates</div><p>Lorem ipsum dolor sit amet consectetur</p></div>
  <div class="teaser"><h4>Velit Maruis?</h4><div class="slot">Some imagery that relates</div><p>Pellentesque velit mauris eleifend et malesuada</p></div>
  <div class="teaser"><h4>Suspendisse feugiat</h4><div class="slot">Some imagery that relates</div><p>Suspendisse feugiat odio eu velit varius</p></div>
</section>

<a class="signup">Sign up for your own Ad</a>
<div class="fade"></div>
</body>
</html>
```